International Medical Company Needs a Website Design for a Support Site

We need a website design for a support site we are doing for ostomates called Bright Returns. We are an international company but this website is for our Australian market.

The website is a support site for people who are living with an Ostomy or Bowel Disease. This is a site where they can read other ostomates' stories and how they are dealing with the fact that they have to wear a pouch everyday.

The URL for our US site is: http://www.brightreturnsvale.com/

We need to use the same logo but we have freedom around the color scheme. We are not fond of the brown color scheme used in our US site and are happy for designs to be submitted with alternatives.

• We want the design to be clean, inspiring, modern and inviting.
• We would like to see a design for the mainpage / homepage and one of the subpages
• We only require the PSD / image files (no HTML needed)

Attached to this project is our sitemap, an example wireframe and the logos. We are happy for you to play around with different options and don't have to stick to the layout shown in the wireframe.

If you have any further questions please ask.

```html
<!DOCTYPE html>
<html lang="en">
<head>
<meta charset="utf-8">
<title>Bright Returns – Sharing stories &amp; giving hope</title>
<link rel="stylesheet" href="https://fonts.googleapis.com/css2?family=Arimo:wght@400;700&family=Gelasio:wght@400&display=swap">
<style>
  :root {
    --plum: #45102a;
    --berry: #a22a60;
    --rose: #b3496b;
    --rose-dark: #97304f;
    --sage: #a5c08c;
    --sage-dark: #809c69;
    --mist: #d5dddc;
    --ink: #5a5a5a;
    --ring: #c9c9cb;
    --footer: #262626;
    --white: #ffffff;
  }
  * { box-sizing: border-box; margin: 0; padding: 0; }
  html, body { width: 1200px; height: 1000px; overflow: hidden; background: var(--white); }
  body { position: relative; font-family: "Arimo", Arial, sans-serif; }

  .page {
    position: absolute; left: 125px; top: 18px; width: 960px; height: 962px;
    background: var(--white);
    box-shadow: 0 0 10px rgba(0,0,0,.35);
    overflow: hidden;
  }
  .abs { position: absolute; }

  /* header */
  .site-header { left: 0; top: 0; width: 960px; height: 94px; background: var(--plum); }
  .brand { left: 27px; top: 20px; width: 100px; height: 60px; display: flex; flex-direction: column; align-items: center; justify-content: flex-end; gap: 6px; }
  .brand-dot { width: 26px; height: 26px; border-radius: 50%; border: 1.5px solid rgba(255,255,255,.8); }
  .brand-name { color: var(--white); font-size: 8.5px; letter-spacing: .8px; text-transform: uppercase; white-space: nowrap; }
  .main-nav { left: 150px; top: 61px; display: flex; gap: 0; color: var(--white); font-size: 14px; }
  .main-nav li { list-style: none; margin-right: 11px; display: flex; align-items: center; gap: 6px; }
  .caret { width: 0; height: 0; border-left: 4px solid transparent; border-right: 4px solid transparent; border-top: 5px solid var(--white); }

  .btn {
    display: flex; align-items: center; justify-content: center;
    width: 151px; height: 33px; border-radius: 3px;
    color: var(--white); font-size: 14px;
  }
  .btn-rose { background: linear-gradient(#c65779, var(--rose-dark)); border: 1px solid #8b2b49; }
  .btn-sage { background: linear-gradient(#b5cf9c, var(--sage-dark)); border: 1px solid #728d5c; }

  .header-share { left: 715px; top: 10px; height: 32px; }
  .region-badge {
    left: 886px; top: 8px; width: 36px; height: 36px; border-radius: 50%;
    border: 2px solid var(--white); color: var(--white); font-size: 11px; font-weight: 700;
    display: flex; flex-direction: column; align-items: center; justify-content: center; line-height: 1;
  }
  .region-badge .caret { margin-top: 2px; }
  .search { left: 715px; top: 52px; width: 208px; height: 33px; display: flex; }
  .search-field { flex: 1; background: var(--white); font-size: 14px; color: #555; padding: 9px 12px; }
  .search-btn { width: 34px; background: var(--sage); display: flex; align-items: center; justify-content: center; }

  /* hero */
  .hero { left: 0; top: 94px; width: 960px; height: 285px; background: var(--mist); }
  .hero-photo {
    left: 636px; top: 0; width: 324px; height: 285px;
    background: linear-gradient(100deg, #c9a58f 0%, #e2c1ab 40%, #d8b39c 70%, #b88f79 100%);
    clip-path: polygon(16px 0, 100% 0, 100% 100%, 0 100%);
  }
  .hero-title { left: 147px; top: 36px; font-family: "Gelasio", Georgia, serif; font-size: 36px; color: var(--plum); font-weight: 400; }
  .hero-lede { left: 147px; top: 86px; width: 480px; font-size: 17.5px; line-height: 22px; color: var(--ink); }
  .hero-share { left: 150px; top: 198px; }
  .hero-read { left: 320px; top: 198px; }

  /* feature */
  .feature-wedge { left: 0; top: 379px; }
  .carousel-dots { left: 445px; top: 387px; display: flex; gap: 9px; }
  .carousel-dots span { width: 12px; height: 12px; border-radius: 50%; border: 1px solid #888; background: var(--white); }
  .carousel-dots span.is-active { background: var(--sage); border-color: var(--sage-dark); }
  .feature-title { left: 150px; top: 403px; font-family: "Gelasio", Georgia, serif; font-size: 36px; color: var(--plum); font-weight: 400; }
  .feature-text { left: 150px; top: 452px; width: 680px; font-size: 17.5px; line-height: 22px; color: var(--ink); }
  .feature-share { left: 659px; top: 518px; }
  .section-shadow { left: 0; top: 564px; width: 960px; height: 10px; background: linear-gradient(#cfcfcf, #ffffff); }

  /* teasers */
  .teaser-divider { left: 480px; top: 582px; width: 1px; height: 328px; background: #9a9a9a; }
  .teaser-ring { width: 270px; height: 270px; border-radius: 50%; border: 2px solid var(--ring); top: 582px; }
  .teaser-disc { position: absolute; left: 7px; top: 7px; width: 252px; height: 252px; border-radius: 50%; }
  .teaser-news { left: 148px; }
  .teaser-news .teaser-disc { background: var(--plum); }
  .teaser-about { left: 543px; }
  .teaser-about .teaser-disc { background: var(--berry); }
  .teaser-body { position: absolute; left: 50px; top: 48px; width: 170px; color: var(--white); }
  .teaser-title { font-family: "Gelasio", Georgia, serif; font-size: 23px; font-weight: 400; margin-bottom: 14px; }
  .teaser-text { font-size: 13px; line-height: 15.5px; }
  .teaser-link { display: block; margin-top: 16px; font-size: 13.5px; color: #c9dca4; }
  .news-more { left: 263px; top: 869px; }
  .about-more { left: 659px; top: 869px; }

  /* footer */
  .site-footer {
    left: 0; top: 924px; width: 960px; height: 38px; background: var(--footer);
    display: flex; align-items: center; padding-left: 37px; gap: 12px;
    color: #d8d8d8; font-size: 11.5px;
  }
</style>
</head>
<body>
<div class="page">

  <header class="site-header abs">
    <div class="brand abs">
      <span class="brand-dot"></span>
      <span class="brand-name">Bright Returns</span>
    </div>
    <ul class="main-nav abs">
      <li>About us <span class="caret"></span></li>
      <li>Personal stories <span class="caret"></span></li>
      <li>Tips for Living <span class="caret"></span></li>
      <li>News <span class="caret"></span></li>
      <li>Resources <span class="caret"></span></li>
      <li>Contact us</li>
    </ul>
    <a class="btn btn-rose header-share abs">Share a story</a>
    <div class="region-badge abs">AUS<span class="caret"></span></div>
    <div class="search abs">
      <div class="search-field">Search</div>
      <div class="search-btn">
        <svg width="20" height="20" viewBox="0 0 20 20"><circle cx="8" cy="8" r="6" fill="none" stroke="#45102a" stroke-width="3"/><line x1="12.5" y1="12.5" x2="18" y2="18" stroke="#45102a" stroke-width="3.5" stroke-linecap="round"/></svg>
      </div>
    </div>
  </header>

  <section class="hero abs">
    <div class="hero-photo abs" role="img" aria-label="Close-up portrait photograph of a smiling young man"></div>
    <h1 class="hero-title abs">Sharing stories &amp; giving hope</h1>
    <p class="hero-lede abs">to people around the world who are facing inflammatory bowel disease, colorectal cancer, or have had ostomy surgery.</p>
    <a class="btn btn-rose hero-share abs">Share a story</a>
    <a class="btn btn-sage hero-read abs">Read a story</a>
  </section>

  <svg class="feature-wedge abs" width="131" height="160" viewBox="0 0 131 160"><polygon points="0,0 131,0 0,160" fill="#d5dddc"/></svg>
  <div class="carousel-dots abs"><span class="is-active"></span><span></span><span></span><span></span></div>
  <h2 class="feature-title abs">Share a story</h2>
  <p class="feature-text abs">Lorem ipsum dolor sit amet, consectetur adipiscing elit. Aenean nec tempus enim, non vulputate justo. Nullam vitae quam hendrerit.</p>
  <a class="btn btn-rose feature-share abs">Share a story</a>
  <div class="section-shadow abs"></div>

  <div class="teaser-ring teaser-news abs">
    <div class="teaser-disc">
      <div class="teaser-body">
        <h3 class="teaser-title">Latest News</h3>
        <p class="teaser-text">Lorem ipsum dolor sit amet, consectetur adipiscing elit. Vestibulum id dignissim nisl, a imperdiet dui. Vestibulum laoreet augue a pretium.</p>
        <a class="teaser-link">Read more</a>
      </div>
    </div>
  </div>
  <div class="teaser-divider abs"></div>
  <div class="teaser-ring teaser-about abs">
    <div class="teaser-disc">
      <div class="teaser-body">
        <h3 class="teaser-title">About BR</h3>
        <p class="teaser-text">Lorem ipsum dolor sit amet, consectetur adipiscing elit. Vestibulum id dignissim nisl, a imperdiet dui. Vestibulum laoreet augue a pretium.</p>
        <a class="teaser-link">Find out more</a>
      </div>
    </div>
  </div>
  <a class="btn btn-sage news-more abs">Read more news</a>
  <a class="btn btn-sage about-more abs">Find out more</a>

  <footer class="site-footer abs">
    <span>Legal Notice</span><span>I</span><span>Privacy Policy</span><span>I</span><span>Sitemap</span>
  </footer>

</div>
</body>
</html>
```